Need a design for Loan Site with new age design

We need a design for our site www.fernpivot.in , we deal with different verticals like home loan, personal loan, loan against property and business loans. Feel free to get in touch if you have any questions.

I have like the concept of the drop down on the eye level where consumer is able to select the product they wish and continue with the form https://www.tallowcrest.com/ . They are in the same line of business as we are.

Here are few more designs which i personally like just to get idea about the taste

https://plumweatherly.com/
http://vexlar.com/partners

Industry/Entity Type

Loan

Number of Pages Required

2 page

Colors
34a7d7
add136
faa54b
fbee3e

Requirements
Must have
• I have like the concept of the drop down on the eye level where consumer is able to select the product they wish and continue with the form https://www.tallowcrest.com/ . They are in the same line of business as we are.
• Here are few more designs which i personally like just to get idea about the taste
• https://plumweatherly.com/
• http://vexlar.com/partners

```html
<!DOCTYPE html>
<html lang="en">
<head>
<meta charset="utf-8">
<title>Fern Pivot – Loans</title>
<link href="https://fonts.googleapis.com/css2?family=Noto+Sans:wght@400;700&display=swap" rel="stylesheet">
<style>
:root{
  --blue:#34a7d7;
  --navy:#0f6aa0;
  --deep:#1a4d70;
  --green:#1fad45;
  --panel:#ebebeb;
  --band:#e6e6e6;
  --text:#555;
  --muted:#8a8a8a;
  --white:#fff;
}
*{margin:0;padding:0;box-sizing:border-box}
html,body{width:918px;height:1200px;overflow:hidden;background:var(--white)}
body{font-family:"Noto Sans",sans-serif;color:var(--text);position:relative}
.abs{position:absolute}

.site-header{position:absolute;left:0;top:0;width:918px;height:48px;background:var(--white)}
.brand{position:absolute;left:172px;top:12px;display:flex;align-items:center;gap:6px;color:var(--blue);font-size:15px}
.brand-mark{width:22px;height:22px;background:var(--navy)}
.main-nav{position:absolute;top:16px;left:0;width:918px;height:19px;font-size:9.5px;color:#888}
.main-nav a{position:absolute;top:3px;color:inherit;text-decoration:none}
.main-nav .active{left:392px;top:0;width:47px;height:19px;background:var(--blue);color:var(--white);display:flex;align-items:center;justify-content:center}

.hero{position:absolute;left:0;top:48px;width:918px;height:382px;background:linear-gradient(135deg,#9fb6c2 0%,#6f8fa3 35%,#7fa6bf 60%,#3e6f8e 100%)}
.hero-title{position:absolute;top:62px;width:100%;text-align:center;color:var(--white);font-size:27px}
.hero-sub{position:absolute;top:96px;width:100%;text-align:center;color:var(--white);font-size:17px}
.hero-arrows{position:absolute;left:404px;top:128px}
.finder{position:absolute;left:268px;top:191px;width:382px;height:39px;display:flex;box-shadow:0 1px 3px rgba(0,0,0,.2)}
.select{width:162px;height:39px;background:var(--white);border-right:1px solid #ddd;display:flex;align-items:center;justify-content:space-between;padding:0 10px;font-size:10.5px;color:#999}
.select svg{width:11px;height:7px}
.finder-btn{width:58px;background:var(--green);color:var(--white);font-size:11px;display:flex;align-items:center;justify-content:center}

.card{position:absolute;top:448px;height:166px;background:var(--panel)}
.welcome{left:172px;width:144px}
.welcome h2{height:47px;background:var(--navy);color:var(--white);font-size:16px;padding:14px 10px 0;letter-spacing:.5px}
.small{font-size:6.8px;line-height:10.5px;color:var(--muted)}
.welcome p{padding:8px 10px}
.about{left:330px;width:258px}
.about .photo{position:absolute;left:0;top:0;width:104px;height:166px;background:linear-gradient(120deg,#e0a85a,#7a4a22 55%,#3a2a20)}
.about .body{position:absolute;left:116px;top:6px;width:136px}
.card h3{font-size:13.5px;color:#333;font-weight:700}
.card h4{font-size:9px;color:#444;font-weight:400;margin-bottom:10px}
.services{left:602px;width:144px;padding:6px 11px}
.services ul{list-style:none}
.services li{display:flex;gap:4px;font-size:6.8px;line-height:13px;color:var(--muted);margin-bottom:6px}
.services li svg{flex:none;width:9px;height:9px;margin-top:2px}

.news{position:absolute;left:172px;top:630px;width:280px}
.news-head{height:28px;background:var(--navy);color:var(--white);font-size:11.5px;display:flex;align-items:center;padding-left:6px;position:relative}
.news-head .nav-btn{position:absolute;top:0;width:31px;height:28px;display:flex;align-items:center;justify-content:center;background:#1980bd}
.news-photo{height:162px;background:linear-gradient(160deg,#5b6b73,#c8d4d8 60%,#e8eef0);position:relative}
.news-photo .more{position:absolute;right:0;bottom:0;background:#6d7f88;color:var(--white);font-size:6.5px;padding:2px 6px}
.news h5{font-size:13px;font-weight:400;color:#333;margin-top:4px}
.news .date{font-size:7px;color:#555}
.news .excerpt{font-size:6.8px;color:var(--muted);line-height:9px;margin-top:8px}

.tile{position:absolute;width:140px;height:122px}
.tile-coins{left:466px;top:630px;background:linear-gradient(135deg,#3a3a3a 0%,#d9d9d9 45%,#c9a07a 75%,#eee)}
.tile-family{left:606px;top:630px;background:linear-gradient(180deg,#7fb3e4 0%,#b7d6f2 70%,#6da33a 100%)}
.tile-blog{left:466px;top:752px;background:linear-gradient(180deg,#4f93b8,#3f7fa3);color:var(--white);padding:42px 6px 0}
.tile-blog b{font-size:10px;font-weight:400;display:block;margin-bottom:9px}
.tile-blog p{font-size:6.4px;line-height:8.6px}
.tile-blog u{color:var(--white)}
.tile-most{left:606px;top:752px;background:#969696;color:var(--white)}
.tile-most .btn{position:absolute;left:11px;width:29px;height:29px;background:#7d7d7d;display:flex;align-items:center;justify-content:center}
.tile-most span{position:absolute;left:50px;top:53px;font-size:13px}

.partners{position:absolute;left:0;top:901px;width:918px;height:143px;background:var(--band)}
.partners h2{position:absolute;top:25px;width:100%;text-align:center;color:var(--blue);font-size:16px;letter-spacing:.3px}
.partner{position:absolute;top:79px;font-size:14px;font-weight:700;color:#8a1c1c;display:flex;align-items:center;gap:5px}
.partner i{display:inline-block;width:14px;height:14px;border-radius:50%;background:currentColor}

.cta{position:absolute;left:0;top:1044px;width:918px;height:124px;background:#36a3d6;overflow:hidden}
.bubble{position:absolute;border-radius:50%}
.cta h2{position:absolute;top:22px;width:100%;text-align:center;font-size:18px;font-weight:400;color:var(--white);letter-spacing:.5px}
.cta .btn{position:absolute;left:399px;top:54px;width:119px;height:37px;border-radius:3px;background:var(--green);color:var(--white);font-size:17px;display:flex;align-items:center;justify-content:center;letter-spacing:.5px}

.site-footer{position:absolute;left:0;top:1168px;width:918px;height:32px;background:var(--deep);font-size:8.5px;color:#b9cbd8}
.site-footer a{position:absolute;top:12px;color:inherit;text-decoration:none}
.site-footer .copy{position:absolute;right:172px;top:11px;font-size:6.5px}
</style>
</head>
<body>

<header class="site-header">
  <div class="brand"><span class="brand-mark"></span>Fern Pivot</div>
  <nav class="main-nav">
    <a class="active" href="#">Home</a>
    <a href="#" style="left:457px">Who we are</a>
    <a href="#" style="left:537px">Services</a>
    <a href="#" style="left:601px">Blog</a>
    <a href="#" style="left:649px">Career</a>
    <a href="#" style="left:705px">Reach Us</a>
  </nav>
</header>

<section class="hero" role="img" aria-label="Stacks of coins and pens on financial papers, tinted blue">
  <h1 class="hero-title" style="font-weight:400">Looking For a Secured Or Unsecured Loan?</h1>
  <p class="hero-sub">We will help you get Best Interest Rate</p>
  <svg class="hero-arrows" width="104" height="52" viewBox="0 0 104 52" fill="none" stroke="#fff" stroke-width="1.6" stroke-linecap="round">
    <path d="M8 2 C12 18 14 32 14 48 M8 42 L14 48 L19 41"/>
    <path d="M36 0 L36 48 M30 41 L36 48 L42 41"/>
    <path d="M64 2 C63 18 66 32 66 48 M60 41 L66 48 L71 41"/>
    <path d="M96 2 C92 18 90 32 88 48 M83 41 L88 48 L94 42"/>
  </svg>
  <form class="finder">
    <div class="select">I would like to<svg viewBox="0 0 11 7"><path d="M1 1l4.5 4.5L10 1" stroke="#666" stroke-width="1.3" fill="none"/></svg></div>
    <div class="select">Select a Product<svg viewBox="0 0 11 7"><path d="M1 1l4.5 4.5L10 1" stroke="#666" stroke-width="1.3" fill="none"/></svg></div>
    <div class="finder-btn">Search</div>
  </form>
</section>

<article class="card welcome">
  <h2>WELCOME</h2>
  <p class="small">Frankfurter porchetta tail short ribs, jerky bresaola drumstick filet mignon pig sirloin t-bone alcatra cow rump shoulder. Shank jowl spare ribs pork loin, pastrami kielbasa ribeye pig t-bone swine pork chop meatball beef ribs. Porchetta boudin ball tip prosciutto frankfurter ground round turkey cow, brisket alcatra venison sirloin andouille turducken.</p>
</article>

<article class="card about">
  <div class="photo" role="img" aria-label="Close-up of stacked coins in warm light"></div>
  <div class="body">
    <h3>Who are We</h3>
    <h4>and Our History</h4>
    <p class="small">Landjaeger pork loin meatloaf cow ball tip leberkas tri-tip short loin kielbasa boudin jowl pork belly t-bone shoulder meatball. Fatback filet mignon beef ribs capicola tongue. Bresaola kielbasa shank porchetta pancetta ham pastrami meatloaf kevin short loin alcatra doner. Bresaola cupim prosciutto, filet mignon picanha brisket capicola tenderloin tongue turkey hamburger alcatra.</p>
  </div>
</article>

<article class="card services">
  <h3>Services</h3>
  <h4>with the Best Features</h4>
  <ul>
    <li><svg viewBox="0 0 9 9"><rect x=".5" y=".5" width="8" height="8" fill="none" stroke="#1a6fa5"/><path d="M2 4.5l2 2 4-5" stroke="#1a6fa5" stroke-width="1.4" fill="none"/></svg>Doorstep Deliveries</li>
    <li><svg viewBox="0 0 9 9"><rect x=".5" y=".5" width="8" height="8" fill="none" stroke="#1a6fa5"/><path d="M2 4.5l2 2 4-5" stroke="#1a6fa5" stroke-width="1.4" fill="none"/></svg>Easy Documentation</li>
    <li><svg viewBox="0 0 9 9"><rect x=".5" y=".5" width="8" height="8" fill="none" stroke="#1a6fa5"/><path d="M2 4.5l2 2 4-5" stroke="#1a6fa5" stroke-width="1.4" fill="none"/></svg>Get Approval within 7 business days</li>
    <li><svg viewBox="0 0 9 9"><rect x=".5" y=".5" width="8" height="8" fill="none" stroke="#1a6fa5"/><path d="M2 4.5l2 2 4-5" stroke="#1a6fa5" stroke-width="1.4" fill="none"/></svg>Compare Quote from all major finacial institutions</li>
  </ul>
</article>

<section class="news">
  <div class="news-head">LASTEST NEWS
    <span class="nav-btn" style="left:218px"><svg width="6" height="9" viewBox="0 0 6 9"><path d="M5 1L1.5 4.5 5 8" stroke="#fff" stroke-width="1.3" fill="none"/></svg></span>
    <span class="nav-btn" style="left:249px;background:var(--navy)"><svg width="6" height="9" viewBox="0 0 6 9"><path d="M1 1l3.5 3.5L1 8" stroke="#fff" stroke-width="1.3" fill="none"/></svg></span>
  </div>
  <div class="news-photo" role="img" aria-label="Hand signing a loan document with a pen"><span class="more">Read more</span></div>
  <h5>Amazing Blog Title here</h5>
  <p class="date">May 10, 2016</p>
  <p class="excerpt">Shank jowl spare ribs pork loin, pastrami kielbasa ribeye pig t-bone swine pork chop meatball beef ribs...</p>
</section>

<div class="tile tile-coins" role="img" aria-label="Calculator beside stacks of coins"></div>
<div class="tile tile-family" role="img" aria-label="Family in a field reaching toward a house and a car in the sky"></div>
<div class="tile tile-blog">
  <b>Awesowe Blog Title here</b>
  <p>Porchetta boudin ball tip prosciutto frankfurter ground round turkey cow, brisket alcatra...<u>Read more</u></p>
</div>
<div class="tile tile-most">
  <span class="btn" style="top:29px"><svg width="9" height="6" viewBox="0 0 9 6"><path d="M1 5l3.5-3.5L8 5" stroke="#fff" stroke-width="1.3" fill="none"/></svg></span>
  <span class="btn" style="top:64px"><svg width="9" height="6" viewBox="0 0 9 6"><path d="M1 1l3.5 3.5L8 1" stroke="#fff" stroke-width="1.3" fill="none"/></svg></span>
  <span>MOST VIEW</span>
</div>

<section class="partners">
  <h2>WE WORK WITH ALL PREMIUM FINANCIAL INSTITUTIONS</h2>
  <div class="partner" style="left:141px">Halvern Bank</div>
  <div class="partner" style="left:290px;color:#8e1b2e"><i></i>Corvale Bank</div>
  <div class="partner" style="left:412px;color:#2a3f7a"><i style="color:#e36a1f"></i>Stenmoor Bank</div>
  <div class="partner" style="left:556px;color:#1b5fa8"><i></i>Lutrel Finserv</div>
  <div class="partner" style="left:688px;color:#d0202a"><i style="color:#1b3f7a"></i>Ossary Bank</div>
</section>

<section class="cta">
  <div class="bubble" role="img" aria-label="Briefcase icon" style="left:158px;top:-16px;width:100px;height:100px;background:#4e2a44"></div>
  <div class="bubble" role="img" aria-label="Presentation board icon" style="left:266px;top:52px;width:80px;height:80px;background:#b4b0ad"></div>
  <div class="bubble" role="img" aria-label="Mail icon" style="left:589px;top:-2px;width:72px;height:72px;background:#1f6fd6"></div>
  <div class="bubble" role="img" aria-label="Laptop icon" style="left:652px;top:42px;width:84px;height:84px;background:#3b2c42"></div>
  <div class="bubble" role="img" aria-label="Money bag icon" style="left:747px;top:-7px;width:106px;height:106px;background:#6d3123"></div>
  <h2>What Are You Waiting For?</h2>
  <div class="btn">Inquire now</div>
</section>

<footer class="site-footer">
  <a href="#" style="left:173px">Home</a>
  <a href="#" style="left:220px">Who we are</a>
  <a href="#" style="left:290px">Services</a>
  <a href="#" style="left:347px">Blog</a>
  <a href="#" style="left:387px">Career</a>
  <a href="#" style="left:438px">Reach Us</a>
  <span class="copy">Copyright 2016 Fern Pivot &nbsp;Privacy Policy</span>
</footer>

</body>
</html>
```